Lou Benfield Tennis Academy - New Website

Our business is built around classes for all ages, competitions, and court hire.

There are a few gym style Wordpress templates that I think will have most of the functionality we need, but we don't like the style. We are looking for someone to make us a design that can be implemented as a child theme to one of these gym based Wordpress themes.

We have looked at:

http://stylebazaar.net/item/active-hall-responsive-wordpress-theme/full_screen_preview/7381926?ref=PixDepot
http://www.zulu-layouts.com/item/gym-fitness/demo/?r=pixdepot
http://www.pribo.tf/redirect/?theme=movenow

For style we are looking for something fresh, clean, and vibrant. Our logo is teal and gold with some red, orange, green and yellow.

https://huetray.examplehub.com/Mineral-D-color-theme-837465/
https://huetray.examplehub.com/Lozenge-D-color-theme-619372/
https://huetray.examplehub.com/Palermo-color-theme-57031/

These are the colour schemes we are leaning towards.

Our current website can be seen here www.lbta.com.au
Updates

The new logo design will be uploaded shortly. We don't need any more work done on that.

A rough logo file has been added for you to work with.

Could I please get some submissions that include what the other pages on the website will look like (instead of just the home page).

I think it's really important that we get the look of the product page. See the design pdf for our ideas on the layout of those pages.

***Edit*** Single product pages, I mean. I think the "Classes" page itself will be based a lot on the theme used so I'm less concerned about that. I just want to see what a page will look like that is only for.... Social Tennis (for example)

Target Market(s)

We teach a lot of kids but also many comp players. Everything needs to be very clear and easy to navigate.

Industry/Entity Type

Court

Requirements
Must have
• Custom content types to easily post new things (eg, new programs, new coaches)
Timetable page that is dynamic based on the programs custom type.
Programs page that is dynamic based on the programs custom type.
Coaches page that is dynamic based on the coaches/trainers content type.

Page templates for programs, competitions and a few other things as per pdf.

```html
<!DOCTYPE html>
<html lang="en">
<head>
<meta charset="utf-8">
<title>Competitions – Lou Benfield Tennis Academy</title>
<link rel="stylesheet" href="https://fonts.googleapis.com/css2?family=Cabin:wght@500;600&family=Arimo:wght@400;700&display=swap">
<style>
:root{
  --page:#ffffff;
  --band:#f5f5f5;
  --ink:#222222;
  --heading:#3e3e3e;
  --teal:#2a7f98;
  --link:#1b8fb3;
  --rule:#dcdcdc;
  --orange-top:#f9a436;
  --orange-bot:#e06f00;
  --orange-edge:#c25e00;
  --aqua-top:#43c6dc;
  --aqua-bot:#168ba8;
  --footer:#444444;
  --footer-ink:#e8e8e8;
}
*{box-sizing:border-box;margin:0;padding:0}
html,body{width:998px;height:1200px;overflow:hidden;background:var(--page)}
body{position:relative;font-family:"Arimo",Arial,sans-serif;color:var(--ink);font-size:10px}
.abs{position:absolute}
h1,h2,h3{font-family:"Cabin",sans-serif;font-weight:600;color:var(--heading)}

/* header */
.page-band{left:0;top:0;width:998px;height:131px;background:var(--band)}
.brand-plate{left:0;top:0}
.brand{left:80px;top:22px;display:flex;align-items:center;gap:10px}
.brand-dot{width:26px;height:26px;border-radius:50%;background:var(--teal)}
.brand-name{font-family:"Cabin",sans-serif;font-weight:600;font-size:20px;color:var(--teal);line-height:1}
.nav{left:397px;top:0;width:601px;height:41px;background:#fff;border-bottom:1px solid var(--rule);display:flex;list-style:none}
.nav li{height:40px;border-left:1px solid #e6e6e6;padding-left:9px;line-height:42px;font-size:11.5px;color:#333}
.page-title{left:0;top:80px;width:922px;text-align:center;font-size:20px;color:#333}
.page-intro{left:0;top:111px;width:922px;text-align:center;font-size:10.5px;color:#222}

/* main column */
.section-kicker{left:95px;top:147px;font-family:"Cabin",sans-serif;font-weight:500;font-size:14.5px;color:var(--teal)}
.hero-frame{left:92px;top:174px;width:565px;height:234px;border:1px solid #e4e4e4;padding:5px;background:#fff}
.hero-photo{width:100%;height:100%;background:linear-gradient(120deg,#2f80c8 0%,#6f8a5c 35%,#c8c8c0 55%,#5a7a4a 80%,#8fae6a 100%)}
.block-title{font-size:16px;left:92px}
.plain-list{left:92px;list-style:none;font-size:10px;line-height:20px}
.bullet-list{left:92px;list-style:none;font-size:10px;line-height:20px;width:540px}
.bullet-list li{position:relative;padding-left:14px}
.bullet-list li::before{content:"";position:absolute;left:1px;top:7px;border-left:4px solid #e8732a;border-top:3px solid transparent;border-bottom:3px solid transparent}
.bullet-list li.wrap{line-height:13px;padding-top:3px;padding-bottom:4px}
.dotted{left:92px;width:566px;border-top:1px dotted #9a9a9a}
.solid{border-top:1px solid #e2e2e2}
.action-btn{top:980px;height:32px;border:1px solid var(--orange-edge);border-radius:3px;background:linear-gradient(var(--orange-top),var(--orange-bot));color:#fff;font-family:"Cabin",sans-serif;font-weight:500;font-size:14px;text-align:center;line-height:30px;box-shadow:inset 0 1px 0 rgba(255,255,255,.35)}
.explore-btn{left:285px;top:1071px;width:193px;height:51px;border:1px solid #1a7f97;border-radius:13px;background:linear-gradient(var(--aqua-top),var(--aqua-bot));color:#fff;font-family:"Cabin",sans-serif;font-weight:500;font-size:16px;text-align:center;line-height:49px;box-shadow:0 1px 2px rgba(0,0,0,.2)}

/* sidebar */
.side-title{font-size:14.5px;letter-spacing:.2px}
.potm-frame{left:672px;top:189px;width:237px;height:135px;border:1px solid #e4e4e4;padding:6px;background:#fff}
.potm-photo{width:100%;height:100%;background:linear-gradient(135deg,#b8a58a 0%,#e9e6e2 40%,#8cae7a 75%,#6f9a5e 100%)}
.potm-text{left:675px;top:336px;width:236px;font-size:10.5px;line-height:15px;color:#333}
.more-link{left:672px;top:386px;width:235px;text-align:right;font-size:10.5px;color:var(--link)}
.event{left:678px;width:227px}
.event-head{display:flex;justify-content:space-between;font-weight:700;font-size:10px;color:var(--link)}
.event-text{margin-top:5px;font-size:10px;line-height:11.5px;color:#333}
.thumb{width:71px;height:51px;border:1px solid #dedede;padding:3px;background:#fff}
.thumb span{display:block;width:100%;height:100%}
.ad{left:677px;top:927px;width:228px;height:190px;background:linear-gradient(160deg,#2a74c0 0%,#1a5aa6 60%,#124a8c 100%);overflow:hidden}
.ad-headline{left:28px;top:10px;font-family:"Cabin",sans-serif;font-weight:500;font-size:20px;line-height:23px;color:#fff}
.ad-person{left:0;top:95px;width:110px;height:95px;background:linear-gradient(135deg,#2c5d93,#193c66)}
.ad-brand{left:118px;top:120px;display:flex;align-items:center;gap:5px;color:#fff;font-family:"Cabin",sans-serif;font-weight:500;font-size:11px;line-height:12px}
.ad-brand-dot{width:10px;height:10px;border-radius:50%;background:#fff}
.ad-cta{left:122px;top:159px;width:90px;height:17px;background:#1d3f7c;border:1px solid #8fb1e0;color:#fff;font-size:11px;font-style:italic;text-align:center;line-height:15px}

/* footer */
.footer{left:0;top:1151px;width:998px;height:49px;background:var(--footer);color:var(--footer-ink);font-size:11px;text-align:center;line-height:49px}
</style>
</head>
<body>

<header>
  <div class="abs page-band"></div>
  <svg class="abs brand-plate" width="400" height="84" viewBox="0 0 400 84" aria-hidden="true">
    <defs><linearGradient id="plate" x1="0" y1="0" x2="0" y2="1"><stop offset="0" stop-color="#fbfbfb"/><stop offset="1" stop-color="#ececec"/></linearGradient></defs>
    <path d="M0 0H397V41Q380 60 368 76Q364 81 356 81H0Z" fill="url(#plate)" stroke="#d8d8d8"/>
  </svg>
  <div class="abs brand"><span class="brand-dot"></span><span class="brand-name">Lou Benfield Tennis Academy</span></div>
  <ul class="abs nav">
    <li style="width:70px">Coaching</li>
    <li style="width:88px">Competitions</li>
    <li style="width:69px">Court Hire</li>
    <li style="width:66px">Services</li>
    <li style="width:52px">Gallery</li>
    <li style="width:80px">Community</li>
    <li style="width:47px">News</li>
    <li style="width:129px">About</li>
  </ul>
  <h1 class="abs page-title">Competitions</h1>
  <p class="abs page-intro">Lorem Ipsum is simply dummy text of the printing and typesetting industry. Lorem Ipsum has been the industry's standard dummy text ever since.</p>
</header>

<main>
  <h2 class="abs section-kicker">Junior Academy</h2>
  <div class="abs hero-frame"><div class="hero-photo" role="img" aria-label="Junior player in blue hitting a ball while a coach watches at the net"></div></div>

  <h3 class="abs block-title" style="top:424px">Ridgeview Tennis “Hot Shots” Series</h3>
  <ul class="abs plain-list" style="top:452px">
    <li>Saturdays week 4-8</li>
    <li>Red Ball 2 – 3.30pm</li>
    <li>Orange Ball 2 – 3.30pm</li>
    <li>Green Ball 3.30 – 5.30pm</li>
  </ul>
  <div class="abs dotted" style="top:552px"></div>

  <h3 class="abs block-title" style="top:567px">Teen Social Comp</h3>
  <ul class="abs bullet-list" style="top:595px">
    <li>Sundays from week 4-8 each term</li>
    <li>3.00-5.00pm</li>
    <li>Round Robin mixer depending on the number of players each week</li>
    <li>Great opportunity to practise your skills in a fun and relaxed atmosphere with like minded teenagers</li>
    <li>Phone or music player playlist essential for the most fun</li>
    <li>Sausage Sizzle/Music/Prizes</li>
    <li>Students enrolled in Carver/Holt Squads/Private Lessons</li>
    <li>Buy either a book of 4 ($28) or 10 ($63)</li>
  </ul>
  <div class="abs dotted" style="top:775px"></div>

  <h3 class="abs block-title" style="top:792px">HDTA Sunday Comp</h3>
  <ul class="abs bullet-list" style="top:820px;width:530px">
    <li>Sundays at 8.00am and 10.30am</li>
    <li>This comp caters to everyone from beginners to advanced players (over 350 players each term)</li>
    <li class="wrap">Girls/Boys/Mothers/Fathers/Coaches/Aunts/Uncles/Sisters/Brothers. Any combination makes a good team as long as they are of a similar standard</li>
    <li>2 person teams (2 sets doubles &amp; 1 set singles)</li>
    <li>8 weeks per term</li>
    <li>LBTA teams play against other clubs on the North Shore on a home and away basis</li>
  </ul>

  <a class="abs action-btn" style="left:92px;width:97px">View Draw</a>
  <a class="abs action-btn" style="left:200px;width:90px">View Teams</a>
  <a class="abs action-btn" style="left:300px;width:106px">View Schedule</a>
  <a class="abs action-btn" style="left:416px;width:96px">View Scores</a>

  <div class="abs solid" style="left:92px;top:1050px;width:566px"></div>
  <a class="abs explore-btn">Click Here to Explore</a>
</main>

<aside>
  <h3 class="abs side-title" style="left:673px;top:160px">Player of the Month</h3>
  <div class="abs potm-frame"><div class="potm-photo" role="img" aria-label="Player of the month with two coaches at the courts"></div></div>
  <p class="abs potm-text">simply dummy text of the printing and typeset-ting industry. Lorem Ipsum has been the indus-try's standard the printing...</p>
  <a class="abs more-link">More info</a>
  <div class="abs solid" style="left:672px;top:413px;width:235px"></div>

  <h3 class="abs side-title" style="left:678px;top:429px">Upcoming Events</h3>
  <div class="abs event" style="top:464px">
    <div class="event-head"><span>Lorem Ipsum has</span><span>June 30, 2013</span></div>
    <p class="event-text">when an unknown printer took a galley of type and scrambled&nbsp; took a galley ....</p>
  </div>
  <div class="abs dotted" style="left:678px;top:517px;width:229px"></div>
  <div class="abs event" style="top:527px">
    <div class="event-head"><span>Lorem Ipsum has</span><span>June 30, 2013</span></div>
    <p class="event-text">when an unknown printer took a galley of type and scrambled&nbsp; took a galley ....</p>
  </div>
  <div class="abs dotted" style="left:678px;top:583px;width:229px"></div>
  <div class="abs event" style="top:597px">
    <div class="event-head"><span>Lorem Ipsum has</span><span>June 30, 2013</span></div>
    <p class="event-text">when an unknown printer took a galley of type and scrambled&nbsp; took a galley ....</p>
  </div>
  <div class="abs solid" style="left:672px;top:657px;width:235px"></div>

  <h3 class="abs side-title" style="left:681px;top:675px">Photo Gallery</h3>
  <div class="abs thumb" style="left:677px;top:708px"><span role="img" aria-label="Kids with medals" style="background:linear-gradient(135deg,#c9a27c,#3b5f9e)"></span></div>
  <div class="abs thumb" style="left:757px;top:708px"><span role="img" aria-label="Court with net" style="background:linear-gradient(#d9e2ea,#8aa36a)"></span></div>
  <div class="abs thumb" style="left:838px;top:708px"><span role="img" aria-label="Players resting courtside" style="background:linear-gradient(#5a7a4a,#c8c8b8)"></span></div>
  <div class="abs thumb" style="left:677px;top:770px"><span role="img" aria-label="Group on the courts" style="background:linear-gradient(#cfd9e2,#7a9a5a)"></span></div>
  <div class="abs thumb" style="left:757px;top:770px"><span role="img" aria-label="Rackets at the net" style="background:linear-gradient(135deg,#3f8a6a,#d08aa0)"></span></div>
  <div class="abs thumb" style="left:838px;top:770px"><span role="img" aria-label="Ball machine on court" style="background:linear-gradient(#2f5a4a,#5a8a7a)"></span></div>
  <div class="abs thumb" style="left:677px;top:833px"><span role="img" aria-label="Families at an event" style="background:linear-gradient(#6a8a4a,#4a5a7a)"></span></div>
  <div class="abs thumb" style="left:757px;top:833px"><span role="img" aria-label="Crowd on the lawn" style="background:linear-gradient(#5a7a3a,#3a4a3a)"></span></div>
  <div class="abs thumb" style="left:838px;top:833px"><span role="img" aria-label="Child playing on grass" style="background:linear-gradient(#c8c0a8,#9aa86a)"></span></div>
  <div class="abs solid" style="left:677px;top:903px;width:230px"></div>

  <div class="abs ad">
    <p class="abs ad-headline">Do you dream<br>of getting a<br>good night's sleep?</p>
    <div class="abs ad-person" role="img" aria-label="Tired man resting his head on his hand"></div>
    <div class="abs ad-brand"><span class="ad-brand-dot"></span><span>Harbourline<br>Medical Center</span></div>
    <div class="abs ad-cta">we can help</div>
  </div>
</aside>

<footer class="abs footer">48 Kellerman Rd, Westbrook NSW 2099. Tel: (02) 5550-1842 © 2012 LBTA PTY LTD</footer>

</body>
</html>
```